Ledgerforge Studio - WordPress Theme & Logo

Design a logo and Wordpress website design for Ledgerforge Studio. Ledgerforge Studio provides cryptocurrency development services to clients who need a team to create & continue developing a new cryptocurrency or who want to replace their current cryptocurrency development team. more details in the attached document.
Updates

Target Market(s)

Entrepreneurs who are building a business / platform that makes use of an underlying cryptocurrency.

Logo Text

LS or Ledgerforge Studio

Coding

Coded - Design and coding required

Font styles to use
Sans Serif

Requirements
Must have
• Professional logo, complete coded Wordpress theme for all pages, containing all specified links and buttons
Nice to have
• It would be nice if the buttons that are meant to integrate with Dealcurrent contain the necessary code for that. I can provide any necessary Dealcurrent details from my account.
Should not have
• Slow loading time

```html
<!DOCTYPE html>
<html lang="en">
<head>
<meta charset="utf-8">
<title>Ledgerforge Studio</title>
<link rel="stylesheet" href="https://fonts.googleapis.com/css2?family=Montserrat:wght@500;600;700;800&family=Heebo:wght@400;500&display=swap">
<style>
:root{
  --navy:#0e1a2e;
  --navy-deep:#0a1424;
  --blue:#1877f2;
  --blue-mid:#1f4f86;
  --blue-soft:#3f8fe0;
  --hex:#2c5d94;
  --ink:#111;
  --text:#333;
  --muted:#f6f7f9;
  --line:#e6e8ec;
  --white:#fff;
  --star:#f4b400;
}
*{box-sizing:border-box;margin:0;padding:0}
html,body{width:1200px;height:3350px;overflow:hidden}
body{position:relative;font-family:'Heebo',Arial,sans-serif;color:var(--text);background:var(--white)}
.abs{position:absolute}
.heading{font-family:'Montserrat',Arial,sans-serif;font-weight:700;color:var(--ink)}
.btn{position:absolute;display:flex;align-items:center;justify-content:center;background:var(--blue);color:var(--white);font-family:'Montserrat',Arial,sans-serif;font-weight:600;border-radius:30px}

/* header */
.site-header{position:absolute;left:0;top:0;width:1200px;height:72px;background:var(--navy)}
.brand{position:absolute;left:100px;top:16px;display:flex;align-items:center;gap:10px;color:var(--white);font-family:'Montserrat',Arial,sans-serif;font-weight:600;font-size:21px}
.brand i{display:block;width:36px;height:36px;background:var(--white)}
.nav a{position:absolute;top:26px;color:var(--white);font-family:'Montserrat',Arial,sans-serif;font-weight:500;font-size:14px;text-decoration:none}
.flag{position:absolute;left:763px;top:26px}
.header-cta{left:824px;top:6px;width:275px;height:55px;font-size:15px}

/* hero */
.hero{position:absolute;left:0;top:72px;width:1200px;height:546px;background:linear-gradient(100deg,#0c2038 0%,#123556 45%,#0e4b6a 100%);overflow:hidden}
.hero-globe{position:absolute;left:700px;top:0;width:500px;height:546px;background:radial-gradient(circle at 55% 45%,#1b8fa8 0%,#12607f 35%,rgba(14,75,106,0) 70%)}
.hero h1{position:absolute;left:98px;top:100px;font-family:'Montserrat',Arial,sans-serif;font-weight:700;font-size:32px;line-height:41.5px;color:var(--white)}
.hero p{position:absolute;left:98px;top:240px;width:520px;font-size:12px;line-height:23px;color:var(--white)}
.hero-cta{left:99px;top:330px;width:275px;height:53px;font-size:15px}
.hero-next{position:absolute;left:100px;top:497px;color:var(--white);font-size:17px;display:flex;align-items:center;gap:10px}
.hero-count{position:absolute;left:218px;top:470px;color:var(--white);font-family:'Montserrat',Arial,sans-serif;font-weight:700;font-size:62px;display:flex;align-items:center;gap:6px}
.hero-count small{font-size:30px;font-weight:500}
.scroll-cue{position:absolute;left:589px;top:488px}

/* section heads */
.sec-mark{position:absolute;left:590px;width:20px;height:20px;background:var(--blue-mid)}
.sec-label{position:absolute;left:0;width:1200px;text-align:center;font-size:11.5px;color:var(--blue-soft);font-family:'Montserrat',Arial,sans-serif;font-weight:500}
.sec-title{position:absolute;left:0;width:1200px;text-align:center;font-size:40px}

/* feature cards */
.feature{position:absolute;top:810px;width:322px;height:305px;border:1px solid var(--line);text-align:center}
.hex{position:absolute;left:50%;transform:translateX(-50%)}
.feature h3{position:absolute;top:176px;left:0;width:100%;font-size:27px}
.feature p{position:absolute;top:215px;left:30px;right:30px;font-size:15px;line-height:25px;color:var(--text)}

/* about */
.about{position:absolute;left:0;top:1212px;width:1200px;height:468px;background:linear-gradient(90deg,#1d4a7c,#245892)}
.about-photo{position:absolute;left:101px;top:65px;width:451px;height:343px;background:linear-gradient(135deg,#5a6474 0%,#8a7a66 45%,#c9822f 55%,#3d4654 100%)}
.about-text{position:absolute;left:635px;top:93px;width:465px;color:var(--white)}
.about-text .label{font-family:'Montserrat',Arial,sans-serif;font-weight:600;font-size:11.5px}
.about-text h2{font-family:'Montserrat',Arial,sans-serif;font-weight:700;font-size:37px;margin-top:8px}
.about-text p{font-size:14.5px;line-height:27.5px;margin-top:12px}
.btn-outline{position:absolute;left:635px;top:328px;width:154px;height:46px;border:1.5px solid var(--white);border-radius:24px;color:var(--white);display:flex;align-items:center;justify-content:center;font-family:'Montserrat',Arial,sans-serif;font-weight:600;font-size:15px}

/* testimonials */
.testimonials{position:absolute;left:0;top:1680px;width:1200px;height:520px;background:var(--muted)}
.review{position:absolute;top:220px;width:322px;height:220px;background:var(--white);text-align:center;box-shadow:0 2px 8px rgba(0,0,0,.05)}
.avatar{position:absolute;top:-44px;left:50%;transform:translateX(-50%)}
.review h4{position:absolute;top:52px;left:0;width:100%;font-family:'Montserrat',Arial,sans-serif;font-weight:600;font-size:13.5px;color:var(--ink);letter-spacing:.5px}
.stars{position:absolute;top:71px;left:0;width:100%;color:var(--star);font-size:9px;letter-spacing:1px}
.review p{position:absolute;top:90px;left:20px;right:20px;font-size:13.2px;line-height:22.5px}
.quote{position:absolute;bottom:-24px;left:50%;transform:translateX(-50%)}

/* services */
.services-intro{position:absolute;left:180px;top:2370px;width:840px;text-align:center;font-size:14.5px;line-height:27.5px}
.plan{position:absolute;top:2505px;width:317px;height:395px;background:var(--white);box-shadow:0 2px 14px rgba(0,0,0,.08);text-align:center}
.plan h3{position:absolute;left:0;width:100%;font-size:23px;line-height:25px}
.plan ul{position:absolute;top:208px;left:72px;list-style:none;text-align:left;font-size:15px}
.plan li{display:flex;align-items:center;gap:8px;height:31px}
.plan li::before{content:"";width:8px;height:8px;border-radius:50%;background:var(--blue-soft);box-shadow:0 0 0 2px var(--white),0 0 0 3.5px var(--blue-soft)}
.plan .btn{left:68px;top:318px;width:175px;height:45px;font-size:16px}

/* footer */
.site-footer{position:absolute;left:0;top:2985px;width:1200px;height:365px;background:linear-gradient(180deg,var(--navy) 0%,var(--navy-deep) 100%);color:var(--white)}
.footer-brand{position:absolute;left:100px;top:185px;font-family:'Montserrat',Arial,sans-serif;font-weight:500;font-size:22px}
.footer-mark{position:absolute;left:152px;top:55px;width:110px;height:110px;background:var(--white)}
.social{position:absolute;top:253px;display:block;width:17px;height:17px;background:var(--white);border-radius:3px}
.foot-col{position:absolute;top:62px}
.foot-col h5{font-family:'Montserrat',Arial,sans-serif;font-weight:700;font-size:17px;margin-bottom:12px}
.foot-col a{display:block;color:var(--white);text-decoration:none;font-size:15px;line-height:33px}
.email{position:absolute;left:809px;top:103px;width:287px;height:47px;background:var(--white);border-radius:24px;color:#444;font-size:14.5px;display:flex;align-items:center;padding-left:24px}
.subscribe{left:809px;top:163px;width:287px;height:47px;font-size:16px}
.rule{position:absolute;left:100px;top:288px;width:1000px;height:1px;background:rgba(255,255,255,.35)}
.copyright{position:absolute;left:0;top:313px;width:1200px;text-align:center;font-size:14.5px}
</style>
</head>
<body>

<svg width="0" height="0" style="position:absolute">
  <defs>
    <linearGradient id="hexFill" x1="0" y1="0" x2="0" y2="1">
      <stop offset="0" stop-color="#3b78b8"/><stop offset="1" stop-color="#1e4a7c"/>
    </linearGradient>
  </defs>
</svg>

<header class="site-header">
  <div class="brand"><i></i>Ledgerforge Studio</div>
  <nav class="nav">
    <a style="left:339px">ABOUT US</a>
    <a style="left:439px">OUR SERVICES</a>
    <a style="left:570px">TESTIMONIALS</a>
    <a style="left:705px">BLOG</a>
  </nav>
  <svg class="flag" width="36" height="20" viewBox="0 0 36 20">
    <rect width="36" height="20" fill="#1f3f8f"/>
    <path d="M0 0L36 20M36 0L0 20" stroke="#fff" stroke-width="4"/>
    <path d="M18 0V20M0 10H36" stroke="#fff" stroke-width="6"/>
    <path d="M18 0V20M0 10H36" stroke="#d22" stroke-width="3"/>
  </svg>
  <div class="btn header-cta">Schedule a Free Consultation</div>
</header>

<section class="hero">
  <div class="hero-globe" role="img" aria-label="Glowing digital globe over a market chart"></div>
  <h1>YOUR OWN CRYPTOCURRENCY.<br>SECURE, EASY TO USE, AND<br>BUILT BY AN EXPERT TEAM.</h1>
  <p>Ledgerforge Studio adds professionalism to cryptocurrency development. Our done-for-you service covers everything from development and IT operations to ongoing support. You haveaccess to a full team, for less than the typical cost of a single developer</p>
  <div class="btn hero-cta">Schedule a Free Consultation</div>
  <div class="hero-next">Next
    <svg width="26" height="12" viewBox="0 0 26 12"><path d="M0 6H24M19 1l5 5-5 5" stroke="#fff" stroke-width="1.5" fill="none"/></svg>
  </div>
  <div class="hero-count">01<small>/</small>
    <svg width="30" height="30" viewBox="0 0 30 30"><circle cx="15" cy="15" r="13" stroke="#fff" stroke-width="1.5" fill="none"/><path d="M13 9l6 6-6 6" stroke="#fff" stroke-width="1.5" fill="none"/></svg>
  </div>
  <svg class="scroll-cue" width="22" height="40" viewBox="0 0 22 40"><rect x="3" y="1" width="16" height="24" rx="8" stroke="#fff" stroke-width="1.5" fill="none"/><path d="M11 7v5" stroke="#fff" stroke-width="1.5"/><path d="M6 32l5 5 5-5" stroke="#fff" stroke-width="1.5" fill="none"/></svg>
</section>

<!-- why choose -->
<div class="sec-mark" style="top:685px"></div>
<div class="sec-label" style="top:716px">WHY CHOOSE US</div>
<h2 class="heading sec-title" style="top:735px">Why choose Ledgerforge Studio</h2>

<div class="feature" style="left:100px">
  <svg class="hex" style="top:40px" width="104" height="118" viewBox="0 0 104 118"><polygon points="52,0 104,29.5 104,88.5 52,118 0,88.5 0,29.5" fill="url(#hexFill)"/><path d="M34 50h36l-18 28z M34 50l8-9h20l8 9 M42 41l10 9 10-9 M52 50v28" stroke="#fff" stroke-width="2" fill="none"/></svg>
  <h3 class="heading">Value</h3>
  <p>A team of experts, regular updates, and fixed costs</p>
</div>
<div class="feature" style="left:440px">
  <svg class="hex" style="top:40px" width="104" height="118" viewBox="0 0 104 118"><polygon points="52,0 104,29.5 104,88.5 52,118 0,88.5 0,29.5" fill="url(#hexFill)"/><circle cx="50" cy="58" r="14" stroke="#fff" stroke-width="2" fill="none"/><path d="M34 58a16 16 0 0 1 32 0 M60 40h14v10h-14z" stroke="#fff" stroke-width="2" fill="none"/></svg>
  <h3 class="heading">Support</h3>
  <p>Receive advice and other services, beyond development.</p>
</div>
<div class="feature" style="left:779px">
  <svg class="hex" style="top:40px" width="104" height="118" viewBox="0 0 104 118"><polygon points="52,0 104,29.5 104,88.5 52,118 0,88.5 0,29.5" fill="url(#hexFill)"/><circle cx="52" cy="46" r="9" stroke="#fff" stroke-width="2" fill="none"/><path d="M30 80v-12h44v12 M36 68v-6h32v6 M40 80v-6 M52 80v-6 M64 80v-6" stroke="#fff" stroke-width="2" fill="none"/></svg>
  <h3 class="heading">Commitment</h3>
  <p>Enjoy regular updates and<br>new features</p>
</div>

<!-- about -->
<section class="about">
  <div class="about-photo" role="img" aria-label="Business people holding a phone with glowing crypto network icons"></div>
  <div class="about-text">
    <div class="label">ABOUT US</div>
    <h2>Who We Are</h2>
    <p>in addition to creating and enhancing cryptocurrencies for clients, the Ledgerforge Studio team has been running the Veltra cryptocurrency since 2017. We prefer long-term relationships, enabling us to deliver the very highest quality and giving you peace of mind that you've got a professional and trustworthy team at your side.</p>
  </div>
  <div class="btn-outline">Learn More</div>
</section>

<!-- testimonials -->
<section class="testimonials">
  <div class="sec-mark" style="top:67px"></div>
  <div class="sec-label" style="top:98px">CLIENT REVIEW</div>
  <h2 class="heading sec-title" style="top:113px">Testimonials</h2>

  <div class="review" style="left:100px">
    <svg class="avatar" width="96" height="86" viewBox="0 0 96 86" role="img" aria-label="Client portrait"><polygon points="24,0 72,0 96,43 72,86 24,86 0,43" fill="#6f9cc4"/></svg>
    <h4>JORDAN REYES</h4><div class="stars">★★★★★</div>
    <p>At vero eos et accusamus etto odio dignissimos ducimus qui blanditiis praesentium voluptatum deleniti atque corrupti qures et quas molestias excepturi sint occaecati</p>
    <svg class="quote" width="48" height="48" viewBox="0 0 48 48"><circle cx="24" cy="24" r="23" fill="#3c6fb0"/><path d="M14 30c0-7 3-11 8-13v3c-3 1-4 3-4 5h4v6h-8z M26 30c0-7 3-11 8-13v3c-3 1-4 3-4 5h4v6h-8z" fill="#fff"/></svg>
  </div>
  <div class="review" style="left:439px">
    <svg class="avatar" width="96" height="86" viewBox="0 0 96 86" role="img" aria-label="Client portrait"><polygon points="24,0 72,0 96,43 72,86 24,86 0,43" fill="#d9d4cf"/></svg>
    <h4>JORDAN REYES</h4><div class="stars">★★★★★</div>
    <p>At vero eos et accusamus etto odio dignissimos ducimus qui blanditiis praesentium voluptatum deleniti atque corrupti qures et quas molestias excepturi sint occaecati</p>
    <svg class="quote" width="48" height="48" viewBox="0 0 48 48"><circle cx="24" cy="24" r="23" fill="#3c6fb0"/><path d="M14 30c0-7 3-11 8-13v3c-3 1-4 3-4 5h4v6h-8z M26 30c0-7 3-11 8-13v3c-3 1-4 3-4 5h4v6h-8z" fill="#fff"/></svg>
  </div>
  <div class="review" style="left:778px">
    <svg class="avatar" width="96" height="86" viewBox="0 0 96 86" role="img" aria-label="Client portrait"><polygon points="24,0 72,0 96,43 72,86 24,86 0,43" fill="#9aa3ad"/></svg>
    <h4>JORDAN REYES</h4><div class="stars">★★★★★</div>
    <p>At vero eos et accusamus etto odio dignissimos ducimus qui blanditiis praesentium voluptatum deleniti atque corrupti qures et quas molestias excepturi sint occaecati</p>
    <svg class="quote" width="48" height="48" viewBox="0 0 48 48"><circle cx="24" cy="24" r="23" fill="#3c6fb0"/><path d="M14 30c0-7 3-11 8-13v3c-3 1-4 3-4 5h4v6h-8z M26 30c0-7 3-11 8-13v3c-3 1-4 3-4 5h4v6h-8z" fill="#fff"/></svg>
  </div>
</section>

<!-- services -->
<div class="sec-mark" style="top:2260px"></div>
<div class="sec-label" style="top:2292px">OUR SERVICE</div>
<h2 class="heading sec-title" style="top:2308px">What We Do</h2>
<p class="services-intro">Ledgerforge Studio offers more than just development. We provide a complete solution and our clients receive access to expert advice, ongoing support, I.T. operations, mobile wallets, and even the creation of white papers, Our packages can be tailored to suit you to match your requirements or budget, you can simply pick and choose the features you would like. Alternatively, We can create a custom package just for you.</p>

<div class="plan" style="left:100px">
  <svg class="hex" style="top:28px" width="88" height="100" viewBox="0 0 88 100"><polygon points="44,0 88,25 88,75 44,100 0,75 0,25" fill="url(#hexFill)"/><path d="M24 62l-4-22 12 10 12-16 12 16 12-10-4 22z" stroke="#fff" stroke-width="2" fill="none"/></svg>
  <h3 class="heading" style="top:142px">Blockchain<br>Creation &amp; Launch</h3>
  <ul><li>This is a list item</li><li>Another list item</li><li>Yup, another list item</li></ul>
  <div class="btn">Learn More</div>
</div>
<div class="plan" style="left:442px">
  <svg class="hex" style="top:28px" width="88" height="100" viewBox="0 0 88 100"><polygon points="44,0 88,25 88,75 44,100 0,75 0,25" fill="url(#hexFill)"/><path d="M24 58l-4-20 12 9 12-14 12 14 12-9-4 20z M24 64h40" stroke="#fff" stroke-width="2" fill="none"/></svg>
  <h3 class="heading" style="top:167px">Basic</h3>
  <ul><li>This is a list item</li><li>Another list item</li><li>Yup, another list item</li></ul>
  <div class="btn">Learn More</div>
</div>
<div class="plan" style="left:783px">
  <svg class="hex" style="top:28px" width="88" height="100" viewBox="0 0 88 100"><polygon points="44,0 88,25 88,75 44,100 0,75 0,25" fill="url(#hexFill)"/><path d="M24 54l-4-20 12 9 12-14 12 14 12-9-4 20z M24 54h40v12h-40z" stroke="#fff" stroke-width="2" fill="none"/></svg>
  <h3 class="heading" style="top:164px">Mid-range</h3>
  <ul><li>This is a list item</li><li>Another list item</li><li>Yup, another list item</li></ul>
  <div class="btn">Learn More</div>
</div>

<footer class="site-footer">
  <div class="footer-mark"></div>
  <div class="footer-brand">Ledgerforge Studio</div>
  <span class="social" style="left:138px"></span>
  <span class="social" style="left:178px"></span>
  <span class="social" style="left:224px"></span>
  <span class="social" style="left:264px"></span>

  <div class="foot-col" style="left:357px">
    <h5>Site Content</h5>
    <a>Home</a><a>About</a><a>Feature</a><a>Pricing</a><a>Contact</a>
  </div>
  <div class="foot-col" style="left:581px">
    <h5>Major Topics</h5>
    <a>Search</a><a>T&amp;Cs</a><a>Privacy</a><a>Commu</a>
  </div>
  <div class="foot-col" style="left:808px">
    <h5>Get our Newsletter</h5>
  </div>
  <div class="email">Enter your email</div>
  <div class="btn subscribe">SUBSCRIBE</div>

  <div class="rule"></div>
  <div class="copyright">Copyright © 2021 Ledgerforge Studio. All rights reserved.</div>
</footer>

</body>
</html>
```